north lark upkeep services

Target Market(s)

General letter head for emails and letter quotes ect

Colors
0054AA
0677BA
7BADD7
CADEEF
E8F1F8
0094D4
00A9DD
6FCCEA
C7EBF8
E9F6FB

Requirements
Must have
• logo phone email website names
Nice to have
• what we do (from the website)

```html
<!DOCTYPE html>
<html lang="en">
<head>
<meta charset="utf-8">
<title>North Lark Upkeep Services – Letterhead</title>
<link href="https://fonts.googleapis.com/css2?family=Arimo:wght@400;700&display=swap" rel="stylesheet">
<style>
  :root {
    --paper: #f6f4f5;
    --ink: #2b2b2b;
    --ink-soft: #444;
    --brand-navy: #241f5e;
    --brand-blue: #0a8fd1;
    --brand-deep: #0054aa;
    --signature-tone: #cfd3da;
  }
  html, body {
    margin: 0;
    padding: 0;
    width: 942px;
    height: 1200px;
    overflow: hidden;
    background: var(--paper);
  }
  .letterhead {
    position: relative;
    width: 942px;
    height: 1200px;
    background: var(--paper);
    font-family: "Arimo", Arial, sans-serif;
    color: var(--ink);
  }
  .brand {
    position: absolute;
    left: 204px;
    top: 100px;
    display: flex;
    align-items: center;
    gap: 10px;
  }
  .brand-dot {
    width: 22px;
    height: 22px;
    border-radius: 50%;
    background: var(--brand-deep);
  }
  .brand-name {
    font-weight: 700;
    font-size: 17px;
    line-height: 1.2;
    color: var(--brand-deep);
    text-transform: uppercase;
    width: 150px;
  }
  .contact {
    position: absolute;
    left: 633px;
    top: 70px;
    font-size: 14px;
    line-height: 18px;
    color: var(--ink);
  }
  .contact .address { text-transform: uppercase; margin: 0 0 6px; }
  .contact .line { display: flex; align-items: center; gap: 8px; margin: 0; }
  .contact svg { width: 12px; height: 12px; fill: var(--brand-deep); }
  .salutation {
    position: absolute;
    left: 64px;
    top: 296px;
    margin: 0;
    font-size: 25px;
    font-weight: 400;
    color: var(--ink-soft);
  }
  .body-copy {
    position: absolute;
    left: 64px;
    top: 360px;
    width: 813px;
    font-size: 13.4px;
    line-height: 16.2px;
    color: var(--ink);
  }
  .body-copy p { margin: 0 0 18px; text-align: justify; }
  .closing {
    position: absolute;
    left: 64px;
    top: 792px;
    margin: 0;
    font-size: 13.4px;
  }
  .signature {
    position: absolute;
    left: 74px;
    top: 870px;
    width: 126px;
    height: 50px;
    background: linear-gradient(90deg, var(--signature-tone), transparent);
    border-radius: 4px;
  }
  .signatory {
    position: absolute;
    left: 76px;
    top: 940px;
  }
  .signatory .name { margin: 0; font-size: 19px; color: var(--ink-soft); }
  .signatory .role { margin: 4px 0 0; font-size: 14px; color: var(--ink-soft); }
  .footer-band {
    position: absolute;
    left: 0;
    bottom: 0;
    width: 942px;
    height: 30px;
    display: flex;
  }
  .footer-band .web {
    width: 665px;
    background: var(--brand-navy);
    color: #fff;
    font-size: 14px;
    line-height: 30px;
    padding-left: 64px;
    box-sizing: border-box;
  }
  .footer-band .gap { width: 3px; background: var(--paper); }
  .footer-band .accent { flex: 1; background: var(--brand-blue); }
</style>
</head>
<body>
<main class="letterhead">
  <header>
    <div class="brand">
      <span class="brand-dot"></span>
      <span class="brand-name">North Lark Upkeep Services</span>
    </div>
    <address class="contact" style="font-style:normal">
      <p class="address">14 Wren Lane<br>Coral Heights, Queensland<br>4221 Australia</p>
      <p class="line">
        <svg viewBox="0 0 24 24" aria-hidden="true"><path d="M6.6 10.8a15.1 15.1 0 0 0 6.6 6.6l2.2-2.2a1 1 0 0 1 1-.25 11.4 11.4 0 0 0 3.6.57 1 1 0 0 1 1 1V20a1 1 0 0 1-1 1A17 17 0 0 1 3 4a1 1 0 0 1 1-1h3.5a1 1 0 0 1 1 1c0 1.25.2 2.45.57 3.57a1 1 0 0 1-.25 1z"/></svg>
        955-210-4836
      </p>
      <p class="line">
        <svg viewBox="0 0 24 24" aria-hidden="true"><path d="M2 5h20v14H2z M2 5l10 7 10-7" fill="var(--brand-deep)"/><path d="M3 6l9 6.3L21 6" fill="none" stroke="#fff" stroke-width="1.6"/></svg>
        info@northlarkupkeep.com.au
      </p>
    </address>
  </header>

  <h1 class="salutation">Dear Mr. Carter,</h1>

  <section class="body-copy">
    <p>Lorem ipsum dolor sit amet, consectetur adipiscing elit. Donec orci purus, luctus vitae dignissim eu, iaculis sed purus. Vivamus faucibus, ipsum nec aliquet viverra, leo mauris condimentum ligula, sit amet sagittis enim ligula quis arcu. Nam egestas tortor id nisi porttitor mattis. In tortor ante, ultricies in suscipit a, tempus non massa. Vivamus et auctor mi. Fusce vel massa nulla. Phasellus nec eros mauris, et scelerisque orci.</p>
    <p>Donec malesuada orci vitae nulla accumsan porta a id massa. Quisque accumsan iaculis magna sit amet fringilla. Maecenas consequat, magna eget tincidunt semper, odio nibh rutrum mi, id feugiat ante nisi eu risus. Vestibulum nunc orci, rhoncus a placerat in, ultricies in mi. Cras mattis varius eros, vel fringilla nisi suscipit eget. Quisque scelerisque sagittis nulla at porttitor.</p>
    <p>Sed id augue vitae urna euismod commodo aliquet a quam. Pellentesque arcu velit, cursus et malesuada ut, consequat et diam. Nullam erat sem, rhoncus id ullamcorper vitae, rhoncus et arcu. In ultricies ultricies nulla, ut rutrum nisi iaculis at. Donec eu magna a metus ornare faucibus. Fusce aliquet faucibus ultricies. Morbi semper, est id tincidunt gravida, sem arcu adipiscing lacus, ac bibendum nulla leo eu purus. Quisque nec diam sed risus consectetur a ccumsan quis quis nibh. Vestibulum id purus lorem.</p>
    <p>It is a long established fact that a reader will be distracted by the readable content of a page when looking at its layout. The point of using Lorem Ipsum is that it has a more-or-less normal distribution of letters, as opposed to using 'Content here, content here', making it look like readable English. Many desktop publishing packages</p>
  </section>

  <p class="closing">Sincerely,</p>
  <div class="signature" role="img" aria-label="Handwritten signature"></div>
  <div class="signatory">
    <p class="name">Daniel Carter</p>
    <p class="role">CEO/ Founder</p>
  </div>

  <footer class="footer-band">
    <div class="web">www.northlarkupkeep.com.au</div>
    <div class="gap"></div>
    <div class="accent"></div>
  </footer>
</main>
</body>
</html>
```